Word Template for KESTREL Polls

KESTREL Polls stands for 'Kinship Evaluation Study Tracking Regional Everyday Lives Polls'. It is a collaborative research effort to format and combine multiple sources of public opinion data from around the world into merged datasets. We need a Microsoft Word template design for our research reports, dataset codebooks, crowdsourced development guidelines, and other documents that will be produced as part of the research and development. The template should match the website design and logo, which are attached to this contest (these are the files from previous successful design contests).

The main purpose will be to write reports discussing research and analysis. There will be lots data visualizations (bar charts, scatter plots, pie charts, histograms, trend line charts etc.) as well as tables, diargams, and photos mixed in wit all the text. A second purpose will be to write guidebooks to describe processes and teach others how to manage data, find variables, and write code, which will include screenshots and Word are diagrams and figures.

There are some document uploaded as examples for the kinds of things for which we need the template (working papers, codebooks, pamphlets, etc)

Target Market(s)

academia, government, non-profits, postgraduates, researchers

Font styles to use
Serif

Colors

Designer to choose colors to be used in the design.

Requirements
Must have
• A4 size page template
• Cover page
• Must match website design and logo (see attached)
Nice to have
• Colors to match logo and website (see attached)

```html
<!DOCTYPE html>
<html lang="en">
<head>
<meta charset="utf-8">
<title>KESTREL Polls – Proposal Report Cover</title>
<link rel="stylesheet" href="https://fonts.googleapis.com/css2?family=Lato:wght@400;700&display=swap">
<style>
  :root {
    --paper: #f9f9f9;
    --brand-dark: #1f6cb3;
    --brand-light: #22a3de;
    --band: #21a6e0;
    --white: #ffffff;
    --photo-top: #52b8e8;
    --photo-mid: #2d9ad6;
    --photo-deep: #1a7fc0;
  }
  * { margin: 0; padding: 0; box-sizing: border-box; }
  html, body { width: 927px; height: 1200px; overflow: hidden; }
  body { font-family: "Lato", "Calibri", sans-serif; background: var(--paper); }
  .cover { position: relative; width: 927px; height: 1200px; }

  .masthead { position: absolute; top: 0; left: 0; width: 927px; height: 376px; background: var(--paper); }
  .brand {
    position: absolute; right: 41px; top: 220px;
    display: flex; align-items: center; gap: 16px;
  }
  .brand-dot { width: 40px; height: 40px; border-radius: 50%; background: var(--brand-dark); }
  .brand-name { font-size: 44px; font-weight: 700; color: var(--brand-dark); line-height: 1; }
  .doc-type {
    position: absolute; right: 42px; top: 296px;
    font-size: 37px; font-weight: 700; line-height: 1;
  }
  .doc-type .primary { color: var(--brand-dark); }
  .doc-type .secondary { color: var(--brand-light); }

  .title-band {
    position: absolute; top: 376px; left: 0; width: 927px; height: 166px;
    background: var(--band); color: var(--white); text-align: right; padding-right: 39px;
  }
  .title { font-size: 37px; font-weight: 700; padding-top: 43px; line-height: 1; letter-spacing: 0.2px; }
  .author { font-size: 27px; font-weight: 400; margin-top: 14px; line-height: 1; }

  .cover-photo {
    position: absolute; top: 542px; left: 0; width: 927px; height: 658px;
    background: linear-gradient(160deg, var(--photo-top) 0%, var(--photo-mid) 45%, var(--photo-deep) 75%, var(--photo-top) 100%);
  }
</style>
</head>
<body>
<main class="cover">
  <header class="masthead">
    <div class="brand">
      <span class="brand-dot"></span>
      <span class="brand-name">KESTREL Polls</span>
    </div>
    <p class="doc-type"><span class="primary">Proposal</span> <span class="secondary">Report</span></p>
  </header>

  <section class="title-band">
    <h1 class="title">MAIN HEADING TITLE HERE</h1>
    <p class="author">Author/presented name</p>
  </section>

  <div class="cover-photo" role="img" aria-label="Blue-tinted photo of two business people at a desk reviewing a tablet, with a glass of water and printed bar charts"></div>
</main>
</body>
</html>
```